Geschäftspapiere für Rechtsanwaltskanzlei
Zielgruppe
Rechtsanwaltskanzlei als Einzelkanzlei, Schwerpunkt: Immobilienrecht
Aufgabenstellung
Das Design soll modern abstrakt sein und Stärke und Kompromisslosigkeit assoziieren ( wie das bereits vorhandene Logo). Die Informationen im vorhandenen Briefbogen müssen alle übernommen werden.
Wir benötigen 4 Betreffzeilen: Unser Zeichen, Ihr Zeichen, wer ./.wen und kurze Beschreibung des Falles.
Das schwarze Logo soll übernommen werden, gerne hätten wir noch eine zweite Farbe ( rot oder blau ) im Briefbogen in Form von Balken oder Hervorhebung von Text.

```html
<!DOCTYPE html>
<html lang="de">
<head>
<meta charset="utf-8">
<title>Briefbogen – Kessler Rechtsanwaltskanzlei</title>
<link href="https://fonts.googleapis.com/css2?family=Carlito:wght@400;700&display=swap" rel="stylesheet">
<style>
  :root {
    --paper: #ffffff;
    --ink: #111111;
    --brand-ink: #1a1a1a;
    --rule: #9aa3ad;
    --accent-blue: #5b9bd5;
    --footer-ink: #333333;
  }
  * { margin: 0; padding: 0; box-sizing: border-box; }
  html, body { width: 895px; height: 1200px; overflow: hidden; background: var(--paper); }
  body { font-family: "Carlito", "Calibri", sans-serif; color: var(--ink); }
  .letterhead { position: relative; width: 895px; height: 1200px; background: var(--paper); }

  .accent-bar { position: absolute; left: 0; top: 0; width: 14px; height: 1200px; background: var(--accent-blue); }

  .brand { position: absolute; left: 566px; top: 112px; display: flex; align-items: center; gap: 10px; }
  .brand-square { width: 22px; height: 22px; background: var(--brand-ink); }
  .brand-name { font-size: 18px; font-weight: 700; color: var(--brand-ink); white-space: nowrap; }
  .brand-rule { position: absolute; left: 418px; top: 163px; width: 440px; height: 2px; background: var(--rule); }

  .recipient, .references, .sender { position: absolute; font-size: 11px; line-height: 12.7px; font-style: normal; }
  .recipient { left: 128px; top: 196px; }
  .references { left: 428px; top: 196px; font-weight: 700; }
  .sender { left: 428px; top: 264px; }
  .sender a { color: var(--ink); text-decoration: underline; }

  .subject { position: absolute; left: 128px; top: 400px; width: 730px; padding-left: 10px;
    border-left: 3px solid var(--accent-blue); font-size: 11px; line-height: 16px; }
  .subject-row { display: flex; }
  .subject-label { width: 150px; font-weight: 700; color: var(--accent-blue); }

  .footer-rule { position: absolute; left: 128px; top: 1016px; width: 730px; height: 3px; background: var(--accent-blue); }
  .footer { position: absolute; top: 1034px; left: 0; width: 100%; font-size: 11px; line-height: 14px; color: var(--footer-ink); }
  .footer-col { position: absolute; top: 0; }
  .footer-col h2 { font-size: 11px; font-weight: 700; color: var(--accent-blue); margin-bottom: 14px; }
  .office-muelheim { left: 128px; }
  .office-dellbrueck { left: 360px; }
  .bank { left: 590px; }
</style>
</head>
<body>
<main class="letterhead">
  <div class="accent-bar"></div>

  <header class="brand">
    <span class="brand-square"></span>
    <span class="brand-name">Kessler Rechtsanwaltskanzlei</span>
  </header>
  <div class="brand-rule"></div>

  <address class="recipient">
    Empfänger<br>Adresse<br>PLZ/Ort
  </address>

  <div class="references">
    Ihr Zeichen/Ihre Nachricht vom:<br>
    Unser Zeichen/Unsere Nachricht vom:<br>
    Telefon | Name:
  </div>

  <address class="sender">
    Kessler Rechtsanwaltskanzlei<br>
    Marlene Vosskamp-Reiter<br>
    Fachanwältin für Mietrecht und Wohnungseigentumsrecht<br>
    Lindenhofer Weg 212b<br>
    51069 Köln<br>
    E-Mail: post@kessler-kanzlei.de<br>
    FAX: +49 (0) 221 555 01 20<br>
    <a href="#">www.kessler-kanzlei.de</a>
  </address>

  <section class="subject">
    <div class="subject-row"><span class="subject-label">Unser Zeichen:</span><span></span></div>
    <div class="subject-row"><span class="subject-label">Ihr Zeichen:</span><span></span></div>
    <div class="subject-row"><span class="subject-label">Wer ./. Wen:</span><span></span></div>
    <div class="subject-row"><span class="subject-label">Betreff:</span><span></span></div>
  </section>

  <div class="footer-rule"></div>
  <footer class="footer">
    <section class="footer-col office-muelheim">
      <h2>Büro Köln-Mülheim</h2>
      Ahornallee 38<br>51063 Köln<br>Tel.: +49 (0) 221 555 01 10<br>FAX: +49 (0) 221 555 01 20
    </section>
    <section class="footer-col office-dellbrueck">
      <h2>Büro Köln Dellbrück.</h2>
      Lindenhofer Weg 212b<br>51069 Köln<br>Tel.: +49 (0) 221 555 0130<br>FAX: +49 (0) 221 555 01 20
    </section>
    <section class="footer-col bank">
      <h2>Bankverbindung:</h2>
      Stadtsparkasse Rheinufer<br>DE12 3704 0000 0045 6789 01<br>BIC: RHUFDE33XXX
    </section>
  </footer>
</main>
</body>
</html>
```